TR Advisory Business Cards - High End AV / Low Voltage Company

We are low voltage AV company that specializes in high end clients on the residential side and larger businesses on the commercial side. We want something modern, tech looking but also something that is extremely professional looking. We have uploaded our logos and postcards we already have in the field. Along with a picture of one of our wrapped vans. Our website is at www.trvadvisory.example and our primary colors are the orange, green, grey and blue all military color finishes.

We are interesting in the slogans "Pairing You with the Right Technology" or "Leading the Lowcountry in Tech"

Target Market(s)

We focus on 70% Commercial and 30% Residential Customers

Industry/Entity Type

Low Voltage, AV Company

Contact Information for Business Card

Name - Dorian Fairweather, Title - Owner, Office Phone - 555-714-3096, Mobile Phone - 555-802-4173, E-Mail - d@trvadvisory.example, Website: www.trvadvisory.example

Font styles to use
Sans Serif

Requirements
Must have
• Must have Name, Title, Work Phone & Mobile, Website and Logo.
Nice to have
• We want something that will impress our higher end clients with a great logo
Should not have
• Too traditional or plain.

```html
<!DOCTYPE html>
<html lang="en">
<head>
<meta charset="utf-8">
<title>TR Advisory Business Cards</title>
<link href="https://fonts.googleapis.com/css2?family=Nunito:wght@400;600;700&display=swap" rel="stylesheet">
<style>
  :root {
    --backdrop: #c9c9c9;
    --card: #ffffff;
    --brand-orange: #ec6837;
    --ink: #1e1e1e;
    --on-orange: #ffffff;
    --on-orange-soft: #fde3d6;
    --pattern-base: #ededed;
    --pattern-tone: #dcdcdc;
  }
  * { box-sizing: border-box; margin: 0; padding: 0; }
  html, body { width: 1200px; height: 1200px; overflow: hidden; }
  body {
    background: var(--backdrop);
    font-family: "Nunito", "Helvetica Neue", Arial, sans-serif;
    position: relative;
  }
  .card {
    position: absolute;
    left: 170px;
    width: 860px;
    height: 504px;
    background: var(--card);
    overflow: hidden;
  }
  .card--front { top: 76px; }
  .card--back { top: 611px; }

  .brand-name {
    position: absolute;
    color: var(--brand-orange);
    font-weight: 700;
    white-space: nowrap;
    transform: translate(-50%, -50%);
    letter-spacing: 0.5px;
  }
  .card--front .brand-name { left: 205px; top: 255px; font-size: 42px; }
  .card--back .brand-name { left: 430px; top: 215px; font-size: 60px; }

  .contact-panel {
    position: absolute;
    left: 385px;
    top: 0;
    width: 420px;
    height: 100%;
    background: var(--brand-orange);
    color: var(--on-orange);
  }
  .pattern-strip {
    position: absolute;
    right: 0;
    top: 0;
    width: 55px;
    height: 100%;
    background: linear-gradient(180deg, var(--pattern-base), var(--pattern-tone) 50%, var(--pattern-base));
  }
  .person-name {
    position: absolute;
    left: 39px;
    top: 134px;
    font-size: 31px;
    font-weight: 600;
    letter-spacing: 1px;
    text-transform: uppercase;
  }
  .person-title {
    position: absolute;
    left: 39px;
    top: 178px;
    font-size: 20px;
    color: var(--on-orange-soft);
  }
  .contact-list {
    position: absolute;
    left: 39px;
    top: 247px;
    list-style: none;
  }
  .contact-item {
    display: flex;
    align-items: center;
    height: 33.5px;
    font-size: 22px;
    letter-spacing: 0.3px;
  }
  .contact-icon {
    width: 16px;
    height: 16px;
    margin-right: 18px;
    flex: none;
  }
  .tagline {
    position: absolute;
    left: 0;
    width: 100%;
    top: 368px;
    text-align: center;
    font-size: 25px;
    color: var(--ink);
  }
  .tagline-rule {
    position: absolute;
    left: 242px;
    top: 435px;
    width: 378px;
    height: 2px;
    background: var(--brand-orange);
  }
</style>
</head>
<body>

<section class="card card--front">
  <div class="brand-name">TR Advisory</div>
  <div class="contact-panel">
    <h1 class="person-name">Dorian Fairweather</h1>
    <p class="person-title">Owner</p>
    <ul class="contact-list">
      <li class="contact-item">
        <svg class="contact-icon" viewBox="0 0 16 16" aria-hidden="true"><path fill="#fff" d="M3.2 1.5l2.3 2.8-1.2 1.6c.9 1.9 2.3 3.3 4.2 4.2l1.6-1.2 2.8 2.3-1.3 2.3C6.6 15 1 9.4 1.5 2.8z"/></svg>
        <span>555-714-3096</span>
      </li>
      <li class="contact-item">
        <svg class="contact-icon" viewBox="0 0 16 16" aria-hidden="true"><rect x="4" y="1" width="8" height="14" rx="1.5" fill="none" stroke="#fff" stroke-width="1.6"/><circle cx="8" cy="12.3" r="0.9" fill="#fff"/></svg>
        <span>555-802-4173</span>
      </li>
      <li class="contact-item">
        <svg class="contact-icon" viewBox="0 0 16 16" aria-hidden="true"><rect x="1" y="3" width="14" height="10" rx="1" fill="#fff"/><path d="M1.5 3.8L8 8.6l6.5-4.8" fill="none" stroke="#ec6837" stroke-width="1.3"/></svg>
        <span>d@trvadvisory.example</span>
      </li>
      <li class="contact-item">
        <svg class="contact-icon" viewBox="0 0 16 16" aria-hidden="true"><g fill="none" stroke="#fff" stroke-width="1.3"><circle cx="8" cy="8" r="6.5"/><ellipse cx="8" cy="8" rx="3" ry="6.5"/><path d="M1.5 8h13M2.5 4.8h11M2.5 11.2h11"/></g></svg>
        <span>www.trvadvisory.example</span>
      </li>
    </ul>
  </div>
  <div class="pattern-strip" role="img" aria-label="Decorative pattern of light grey overlapping arcs"></div>
</section>

<section class="card card--back">
  <div class="brand-name">TR Advisory</div>
  <p class="tagline">Pairing You with the Right Technology</p>
  <div class="tagline-rule"></div>
</section>

</body>
</html>
```